Flyer-Design für Service-Plattform für Vor-Ort-Apotheken
Zielgruppe
Wir entwickeln eine Service-Plattform für Vor-Ort-Apotheken, über die Kunden bei Apotheken in der Umgebung online Medikamente kaufen und sich von den Apotheken über einen Livechat beraten lassen können.
Der Flyer soll ein Vertriebsflyer für die Apotheken werden.
Aufgabenstellung
Wir möchten, dass der Flyer vom Design her nicht zu formell wird, sondern möchten auch ein bisschen 'coolen Startup-Charakter' rüberbringen. Der Flyer soll ein zwei-Blatt-Flyer werden.
Ich werde noch einen ersten Entwurf anfügen, der uns leider nicht sehr angesprochen hat, da dieser einfach zu langweilig wirkte.
Die Roadmap im Flyer gefällt uns wirklich sehr gut, der Rest sollte mit Icons versehen werden und eventuell auch prägnante Worte sollten hervorgehoben werden.
Der Blauton ist auch der Ton, den wir auf unserer Website für Header und Footer verwenden, jedoch fehlte uns im ersten Entwurf des Flyers der Grünanteil (z.B. aus unserem Logo).
Falls es noch Fragen oder Anregungen gibt, bitte einfach melden :)!

```html
<!DOCTYPE html>
<html lang="de">
<head>
<meta charset="utf-8">
<title>Apovia Flyer</title>
<link href="https://fonts.googleapis.com/css2?family=Fira+Sans+Condensed:wght@400;500;700&family=Fira+Sans+Extra+Condensed:wght@400&family=Fira+Sans:wght@400&family=Raleway:wght@300&display=swap" rel="stylesheet">
<style>
  :root{
    --blue:#3ba0d0;
    --green:#8dc043;
    --green-light:#d2e09a;
    --ink:#4a4a55;
    --text:#5a5a5a;
    --label:#6e6e6e;
    --stage:#c3bfbe;
    --white:#ffffff;
  }
  *{margin:0;padding:0;box-sizing:border-box}
  html,body{width:1200px;height:1167px;overflow:hidden;background:var(--stage)}
  .canvas{position:relative;width:1200px;height:1167px;background:var(--stage)}
  .panel{position:absolute;top:9px;height:1148px;overflow:hidden;background:var(--blue)}
  .panel--front{left:15px;width:575px}
  .panel--back{left:618px;width:571px}
  .panel-bg{position:absolute;inset:0;width:100%;height:100%}
  .abs{position:absolute}
  .wordmark{font-family:"Raleway",sans-serif;font-weight:300;font-size:60px;line-height:1;color:var(--ink);letter-spacing:3px;top:60px}
  .brand-square{width:58px;height:58px;background:var(--green);top:24px;border-radius:4px}
  .tagline{font-family:"Fira Sans Extra Condensed",sans-serif;font-size:30px;line-height:1.2;color:var(--white);top:149px}
  .headline{font-family:"Fira Sans Condensed",sans-serif;font-weight:700;color:var(--green);letter-spacing:2.5px;text-transform:uppercase}
  .headline--lg{font-size:31px;line-height:37px;text-align:center;left:20px;width:520px}
  .headline--sm{font-size:20.5px;line-height:24px;letter-spacing:1.3px;white-space:nowrap}
  .headline--xl{font-size:31px;line-height:38px;letter-spacing:1.5px}
  .body{font-family:"Raleway",sans-serif;font-weight:300;color:var(--text);font-size:16.4px;line-height:22.8px;text-align:justify;hyphens:auto;-webkit-hyphens:auto}
  .body--tight{letter-spacing:-0.35px}
  .body--left{text-align:left}
  .step-num{font-family:"Fira Sans Condensed",sans-serif;font-weight:700;font-size:68px;line-height:1;color:var(--green)}
  .step-label{font-family:"Fira Sans Condensed",sans-serif;font-weight:500;font-size:19px;line-height:20px;color:var(--label);text-align:center;width:160px;transform:translateX(-50%)}
  .icon-fill{position:absolute;border-radius:12px;background:linear-gradient(135deg,var(--green),var(--green-light))}
  .web{font-family:"Fira Sans",sans-serif;font-size:43px;line-height:1;color:var(--white);right:60px;top:1084px}
  .contact{font-family:"Fira Sans",sans-serif;font-size:22px;line-height:22px;color:var(--white);left:347px;top:1068px}
</style>
</head>
<body>
<div class="canvas">

  <section class="panel panel--front">
    <svg class="panel-bg" viewBox="0 0 937 1871" preserveAspectRatio="none" aria-hidden="true">
      <path fill="#ffffff" d="M0,0 H683 V333 C683,262 640,216 560,216 H190 C80,216 0,170 0,110 Z"/>
      <path fill="#ffffff" d="M0,333 H780 C870,333 937,390 937,446 V1826 C937,1780 880,1721 800,1721 H180 C70,1721 0,1640 0,1526 Z"/>
    </svg>

    <div class="abs wordmark" style="left:107px">Apovia</div>
    <div class="abs brand-square" style="left:398px"></div>
    <div class="abs tagline" style="left:107px">Tipp dich gesund</div>

    <h1 class="abs headline headline--lg" style="top:249px">Apovia ist unsere<br>Serviceplattform</h1>
    <p class="abs body" style="left:55px;width:442px;top:323px">um Ihre lokale Apotheke mit Kunden digital und persön&shy;lich zusammenzubringen. Neben einem modernen Shopsysem lässt sich durch umfangreiche Service- und Beratungsfunktionen die Persönlichkeit Ihrer Apotheke erleben. Apovia bietet eine bedarfgerechte Kundenbera&shy;tung, Empfehlungs-, Angebots- und Bonus-Systematiken, Notdienst-Suche, digitale Rezept-Vermittlung und mehr.</p>

    <h2 class="abs headline headline--lg" style="top:528px">Kundenzufriedenheit<br>in 4 Schritten</h2>

    <div class="abs step-num" style="left:259px;top:614px">1</div>
    <div class="icon-fill" role="img" aria-label="Icon: Apotheke suchen" style="left:304px;top:609px;width:86px;height:89px"></div>
    <div class="abs step-label" style="left:348px;top:706px">APOTHEKE<br>FINDEN</div>

    <div class="icon-fill" role="img" aria-label="Icon: Sprechblase" style="left:117px;top:698px;width:61px;height:56px"></div>
    <div class="icon-fill" role="img" aria-label="Icon: beratende Person" style="left:169px;top:714px;width:72px;height:85px"></div>
    <div class="abs step-num" style="left:105px;top:772px">2</div>
    <div class="abs step-label" style="left:204px;top:807px">BERATEN<br>LASSEN</div>

    <div class="abs step-num" style="left:342px;top:802px">3</div>
    <div class="icon-fill" role="img" aria-label="Icon: Medikamentendose mit Kapseln" style="left:402px;top:786px;width:77px;height:83px"></div>
    <div class="abs step-label" style="left:433px;top:881px">MEDIKAMENTE<br>BESTELLEN</div>

    <div class="abs step-num" style="left:136px;top:915px">4</div>
    <div class="icon-fill" role="img" aria-label="Icon: Hand hält Einkaufstasche" style="left:187px;top:887px;width:92px;height:98px"></div>
    <div class="abs step-label" style="left:226px;top:995px">BESTELLUNG<br>ABHOLEN</div>

    <div class="abs web">www.apovia.de</div>
  </section>

  <section class="panel panel--back">
    <svg class="panel-bg" viewBox="0 0 931 1871" preserveAspectRatio="none" aria-hidden="true">
      <path fill="#ffffff" d="M0,0 H680 V333 C680,262 637,216 557,216 H190 C80,216 0,170 0,110 Z"/>
      <path fill="#ffffff" d="M0,333 H775 C865,333 931,390 931,446 V1826 C931,1780 875,1721 795,1721 H180 C70,1721 0,1640 0,1526 Z"/>
    </svg>

    <div class="abs wordmark" style="left:109px">Apovia</div>
    <div class="abs brand-square" style="left:398px"></div>
    <div class="abs tagline" style="left:109px">Ihre Vorteile</div>

    <div class="icon-fill" role="img" aria-label="Icon: Personengruppe mit Sprechblasen" style="left:42px;top:225px;width:153px;height:135px"></div>
    <h3 class="abs headline headline--sm" style="left:238px;top:248px">Kundenbeziehung stärken</h3>
    <p class="abs body body--tight" style="left:238px;width:292px;top:278px">Im Fokus der Serviceplattform steht der Auf- und Ausbau einer langfristigen Bezie&shy;hung zwischen Kunden und Apotheke.</p>

    <h3 class="abs headline headline--sm" style="left:26px;top:393px">Wettbewerbsfähigkeit ausbauen</h3>
    <p class="abs body body--tight body--left" style="left:26px;width:362px;top:427px">Die Wettbewerbsposition gegenüber digitalen Ver&shy;sand-Apotheken wird gestärkt. Apovia vereint die Vorteile des Versandhandels mit den persönlichen Stärken der lokalen Apotheke</p>
    <div class="icon-fill" role="img" aria-label="Icon: Berg mit Gipfelfahne" style="left:401px;top:366px;width:144px;height:129px"></div>

    <div class="icon-fill" role="img" aria-label="Icon: steigendes Wachstum" style="left:19px;top:543px;width:144px;height:113px"></div>
    <h3 class="abs headline headline--sm" style="left:191px;top:547px">Kunden- und Umsatzgewinnung</h3>
    <p class="abs body body--tight" style="left:191px;width:339px;top:589px">Die digitale und mobile Kundenansprache er&shy;schließt sneue Zielgruppen und steigert den Umsatz im</p>

    <h3 class="abs headline headline--sm" style="left:33px;top:691px">Gemeinsam in die Zukunft</h3>
    <p class="abs body body--tight" style="left:33px;width:276px;top:726px">Apovia begleitet die lokale Apotheke in eine digitale Zukunft. Mit Apovia verbinden sich Partner des E-Health Marktes, um geimeinsam im lokalen Gesundheitsmarkt zu wachsen</p>
    <div class="icon-fill" role="img" aria-label="Icon: startende Rakete" style="left:349px;top:672px;width:150px;height:151px"></div>

    <div class="icon-fill" role="img" aria-label="Icon: Personengruppe" style="left:8px;top:893px;width:218px;height:120px"></div>
    <h3 class="abs headline headline--xl" style="left:235px;top:863px">Wachse gemeinsam<br>mit Apovia</h3>
    <p class="abs body body--tight body--left" style="left:235px;width:310px;top:952px">Begleiten Sie uns beim Ausbau unserer Ser&shy;viceplattform Apovia und nehmen Sie we&shy;sentlichen Einfluss auf die Richtung, die wir gemeinsam einschlagen</p>

    <div class="abs contact">0170 38294615<br>info@apovia.de<br>www.apovia.de</div>
  </section>

</div>
</body>
</html>
```